KT Appraisals BV business cards (a financial services company)

I am looking for a business card design that stands out in the financial advisory field of business & intellectual property valuation. The business card design should be conservative, yet different. Address details have changed since the attached business card. New address is:

Dorpelstraat 27
4817 KM Leiden
The Netherlands

Telephone number remains the same.

```html
<!DOCTYPE html>
<html lang="en">
<head>
<meta charset="utf-8">
<title>KT Appraisals BV – Business Cards</title>
<link href="https://fonts.googleapis.com/css2?family=Roboto:wght@300;400;500;700&display=swap" rel="stylesheet">
<style>
  :root {
    --stage: #dcdcdc;
    --card-white: #ffffff;
    --ink-dark: #555555;
    --ink-mid: #6a6a6a;
    --ink-light: #b9b9b9;
    --band-grey: #7a7a7a;
    --back-grey-top: #8a8a8a;
    --back-grey-bottom: #5e5e5e;
    --line-white: #ffffff;
  }
  * { box-sizing: border-box; margin: 0; padding: 0; }
  html, body {
    width: 1200px; height: 768px; overflow: hidden;
    background: var(--stage);
    font-family: 'Roboto', sans-serif;
  }
  .stage {
    position: relative; width: 1200px; height: 768px;
  }
  .card {
    position: absolute; top: 230px;
    width: 540px; height: 309px;
    box-shadow: 0 6px 18px rgba(0,0,0,0.25);
    overflow: hidden;
  }
  /* Back side */
  .card-back { left: 40px; }
  .card-back .pattern-field {
    position: absolute; inset: 0;
    background: linear-gradient(160deg, var(--back-grey-top), var(--back-grey-bottom));
  }
  .card-back .back-name {
    position: absolute; right: 28px; bottom: 30px;
    color: var(--line-white);
    font-weight: 300; font-size: 24px; letter-spacing: 1px;
  }
  /* Front side */
  .card-front { left: 620px; background: var(--card-white); }
  .brand {
    position: absolute; left: 30px; top: 78px; width: 250px;
  }
  .brand-box {
    border: 2px solid var(--ink-mid);
    padding: 6px 8px;
    text-align: center;
    color: var(--ink-mid);
    font-weight: 300; font-size: 23px; letter-spacing: 0.5px;
    white-space: nowrap;
  }
  .brand-tagline {
    margin-top: 6px;
    text-align: center;
    color: var(--ink-mid);
    font-weight: 700; font-size: 11.5px; letter-spacing: 1px;
    line-height: 1.25; text-transform: uppercase;
  }
  .contact {
    position: absolute; left: 310px; top: 62px;
    color: var(--ink-mid); font-size: 13px; line-height: 1.35;
  }
  .contact .person {
    color: var(--ink-dark); font-weight: 700; font-size: 18px;
  }
  .contact .person .credentials { font-size: 12px; font-weight: 700; }
  .contact .role {
    color: var(--ink-light); font-size: 13px; margin-bottom: 6px;
  }
  .contact .address { margin-bottom: 4px; }
  .contact-row { display: flex; align-items: center; gap: 8px; }
  .contact-row svg { width: 11px; height: 11px; fill: var(--ink-dark); flex: none; }
  .band {
    position: absolute; left: 0; right: 0; bottom: 0; height: 34px;
    background: var(--band-grey);
  }
  .band span {
    position: absolute; left: 0; right: 0; height: 2px;
    background: var(--line-white);
  }
</style>
</head>
<body>
<main class="stage">
  <section class="card card-back" aria-label="Card back">
    <div class="pattern-field" role="img" aria-label="Repeating brand pattern in grey tones"></div>
    <div class="back-name">KT APPRAISALS BV</div>
  </section>

  <section class="card card-front" aria-label="Card front">
    <div class="brand">
      <div class="brand-box">KT APPRAISALS BV</div>
      <div class="brand-tagline">Business and intellectual<br>property valuations</div>
    </div>

    <div class="contact">
      <div class="person">Martin Vos, <span class="credentials">CFA, ASA, RV</span></div>
      <div class="role">Managing Director</div>
      <div class="address">Dorpelstraat 27<br>4817 KM Leiden<br>The Netherlands</div>
      <div class="contact-row">
        <svg viewBox="0 0 24 24"><path d="M6.6 10.8a15.1 15.1 0 0 0 6.6 6.6l2.2-2.2c.3-.3.7-.4 1-.2 1.1.4 2.3.6 3.6.6.6 0 1 .4 1 1V20c0 .6-.4 1-1 1A17 17 0 0 1 3 4c0-.6.4-1 1-1h3.5c.6 0 1 .4 1 1 0 1.3.2 2.5.6 3.6.1.3 0 .7-.2 1z"/></svg>
        <span>+31(0)70 555 0143</span>
      </div>
      <div class="contact-row">
        <svg viewBox="0 0 24 24"><path d="M2 5h20v14H2z" fill="none"/><path d="M2 5h20v14H2zM4 7v.4l8 5 8-5V7l-8 5z"/></svg>
        <span>mvos@ktappraisals.com</span>
      </div>
      <div class="contact-row">
        <svg viewBox="0 0 24 24"><circle cx="12" cy="12" r="10"/></svg>
        <span>www.ktappraisals.com</span>
      </div>
    </div>

    <div class="band">
      <span style="top:8px"></span>
      <span style="top:15px"></span>
      <span style="top:22px"></span>
    </div>
  </section>
</main>
</body>
</html>
```